Bussines Card - TR EDIFICACIONES, S.A.

We need a design for a business card.
I want it to look professional, but not old fashion.
We are like "young people', somehow i want it to look fresh, new, different, but still serious and professional.
I could use, a non typical design. (I mean, not just rectangular design).

The company Name is " TR EDIFICACIONES, S.A. " we are Panamenian company (spanish language) dedicated to construction and civil engeniering.

The company logo is attached, i use it with white background. Im not sure trying different one, could try.

Industry/Entity Type

Business

```html
<!DOCTYPE html>
<html lang="es">
<head>
<meta charset="utf-8">
<title>TR Edificaciones — Tarjeta de presentación</title>
<link rel="stylesheet" href="https://fonts.googleapis.com/css2?family=Oswald:wght@400;600&family=Exo+2:wght@400;500&display=swap">
<style>
  :root {
    --stage: #1e1e1e;
    --graphite: #5e5e5e;
    --graphite-dark: #4f4f4f;
    --paper: #ffffff;
    --paper-shade: #d8d8d8;
    --sky: #1fa9e6;
    --ink: #555555;
    --white: #ffffff;
  }
  * { margin: 0; padding: 0; box-sizing: border-box; }
  html, body { width: 1200px; height: 863px; overflow: hidden; background: var(--stage); }
  .canvas { position: relative; width: 1200px; height: 863px; }
  .card {
    position: absolute; left: 250px; width: 700px; height: 400px;
    overflow: hidden; box-shadow: 0 10px 30px rgba(0,0,0,.45);
  }
  .card--back { top: 20px; }
  .card--front { top: 443px; }
  .card svg.shapes { position: absolute; inset: 0; }
  .brand { position: absolute; display: flex; align-items: center; gap: 14px; }
  .brand__mark { width: 30px; height: 30px; background: var(--graphite); }
  .brand__name {
    font-family: "Oswald", sans-serif; font-weight: 600; font-size: 17px;
    letter-spacing: 2.5px; color: var(--ink);
  }
  .card--back .brand { left: 50px; top: 186px; }
  .card--front .brand { left: 60px; top: 120px; }
  .website-line {
    position: absolute; left: 420px; top: 140px;
    font-family: "Exo 2", sans-serif; font-size: 19px; letter-spacing: 1px; color: var(--white);
  }
  .person { position: absolute; left: 500px; top: 78px; color: var(--white); }
  .person__name {
    font-family: "Oswald", sans-serif; font-weight: 600; font-size: 36px; letter-spacing: 1px; line-height: 1;
  }
  .person__role {
    font-family: "Exo 2", sans-serif; font-size: 13px; letter-spacing: 2px; margin-top: 6px;
  }
  .address {
    position: absolute; right: 28px; top: 258px; text-align: right;
    font-family: "Exo 2", sans-serif; font-size: 17px; line-height: 1.35; color: var(--white);
  }
  .contacts {
    position: absolute; left: 40px; top: 272px; list-style: none;
    font-family: "Exo 2", sans-serif; font-size: 13px; color: var(--white);
  }
  .contacts li { display: flex; align-items: center; gap: 8px; height: 22px; }
  .contacts svg { width: 12px; height: 12px; fill: var(--white); }
</style>
</head>
<body>
<div class="canvas">

  <section class="card card--back" aria-label="Reverso de la tarjeta">
    <svg class="shapes" viewBox="0 0 700 400" aria-hidden="true">
      <defs>
        <linearGradient id="panelFill" x1="0" y1="0" x2="1" y2="1">
          <stop offset="0" stop-color="#ffffff"/>
          <stop offset="1" stop-color="#d4d4d4"/>
        </linearGradient>
      </defs>
      <rect width="700" height="400" fill="var(--graphite)"/>
      <path d="M0 70 H285 Q310 70 316 94 L360 300 Q366 330 336 330 H0 Z" fill="rgba(0,0,0,.18)" transform="translate(6 6)"/>
      <path d="M0 70 H285 Q310 70 316 94 L360 300 Q366 330 336 330 H0 Z" fill="url(#panelFill)"/>
    </svg>
    <div class="brand">
      <span class="brand__mark"></span>
      <span class="brand__name">TR EDIFICACIONES, S.A.</span>
    </div>
    <p class="website-line">www.tredificaciones.com</p>
  </section>

  <section class="card card--front" aria-label="Anverso de la tarjeta">
    <svg class="shapes" viewBox="0 0 700 400" aria-hidden="true">
      <defs>
        <linearGradient id="paperFill" x1="0" y1="0" x2="1" y2="0">
          <stop offset="0" stop-color="#ffffff"/>
          <stop offset="1" stop-color="#ececec"/>
        </linearGradient>
      </defs>
      <rect width="700" height="400" fill="url(#paperFill)"/>
      <path d="M0 250 H470 L510 230 H700 V400 H0 Z" fill="var(--graphite)"/>
      <path d="M430 130 L560 150 L540 230 Z" fill="var(--paper-shade)" opacity=".7"/>
      <path d="M445 40 H700 V215 H560 Q540 215 532 200 L440 62 Q432 40 445 40 Z" fill="var(--sky)"/>
    </svg>
    <div class="brand">
      <span class="brand__mark"></span>
      <span class="brand__name">TR EDIFICACIONES, S.A.</span>
    </div>
    <div class="person">
      <p class="person__name">DANIEL RIVERA</p>
      <p class="person__role">GERENTE GENERAL</p>
    </div>
    <p class="address">45 Calle Ocho Norte,<br>Edificio 3, Piso 2.</p>
    <ul class="contacts">
      <li><svg viewBox="0 0 12 12"><path d="M2 1h3l1 3-2 1a7 7 0 0 0 3 3l1-2 3 1v3a1 1 0 0 1-1 1A10 10 0 0 1 1 2a1 1 0 0 1 1-1z"/></svg>507 264 1180</li>
      <li><svg viewBox="0 0 12 12"><path d="M3 0h6v12H3zM4 1v8h4V1z"/></svg>507 264 1181</li>
      <li><svg viewBox="0 0 12 12"><path d="M3 0h6v4H3zM1 5h10v5H1zM3 9h6v3H3z"/></svg>507 264 1182</li>
      <li><svg viewBox="0 0 12 12"><path d="M0 2h12v8H0zM1 3l5 4 5-4z"/></svg>info@tredif.com</li>
      <li><svg viewBox="0 0 12 12"><circle cx="6" cy="6" r="6"/></svg>www.tredificaciones.com</li>
    </ul>
  </section>

</div>
</body>
</html>
```